依頼詳細
■サイトマップ
①トップ
②ミナテックについて
③エアコンクリーニング
④水廻りクリーニング
⑤その他クリーニング
⑥フロアコーティング
⑦水廻りコーティング
⑧料金表
⑨実績紹介(一覧)
⑩実績紹介(詳細)
⑪お申し込みの流れ
⑫よくあるご質問
⑬お申し込み・お問い合わせ
⑭ニュース(一覧)
⑮ニュース(詳細)
⑯ブログ(一覧)
⑰ブログ(詳細)
⑱お客様の声(詳細)
⑲お客様の声(詳細)

■優先事項
1.ユーザビリティー
2.凝ったデザイン
3.編集更新

■期待する効果
1.新規顧客の獲得
2.問い合わせ数の向上
3.売上の向上

■ターゲット
【性別】男女比(女性:6.5 男性:3.5)
【年代】20代~40代
【属性】主婦 子連れ 会社員

■素材について
会社ロゴデータ ※後日提供
写真データ(人物・施術内容) ※後日提供

■SNS
トークル 会社用
フォトグラム 会社用 ※取得中

■テイスト
清潔感 優しい シンプル

■デザイン
シンプル(2) 複雑
単色  (4) カラフル
暗い  (4) 明るい
日常  (3) 高級
遊び心 (3) 厳粛
未来的 (3) 伝統的
女性  (2.5) 男性
サイトURL
ページ数
1ページ
希望イメージ
シンプル 複雑
単色 カラフル
暗い 明るい
日常 高級
遊び心 厳粛
未来的 伝統的
女性的 男性的
希望する色
水色系、緑系
納品ファイル
• イラストレーター形式 (.ai)
• フォトショップ形式 (.psd)
• PNG形式 (.png)
補足説明
素材①
サイトマップ・ワイヤーフレーム
http://filebako-demo.jp/download/a81c3e5d0b7f4426c9e2d17f08ab53c6e4f9d021
ダウンロードパスワード pass

素材②
サクモア:https://jp.sakumore-demo.com/
当社で定期契約をしています。クレジット購入のみのもの以外をご利用下さい。
また定期契約のものは弊社の負担となり、ランサー様に負担はありません。
カンプ画像を入れてください。

素材③
現行サイトより引用してください。
URL:http://kumo.hanaten-demo.net/~breeze/minatec/
URL:https://ieyoro-demo.jp/000583921/
画像やテキストに関しては一旦引き抜いて頂いて構いません。
追加で撮影した素材をアップしましたので、
ご確認の上ご使用ください。

http://filebako-demo.jp/download/c27e9a0f4d1b8e3357af6c20d9e1b4a8f05c7e19
ダウンロードパスワード pass
提案がないため延長させて頂きます!
皆様何卒よろしくお願いいたいます。
ご提案が少ないため、延長させて頂きます。
皆様、何卒よろしくお願いいたいます。

素敵なご提案をありがとうございます!

皆様ご提案ありがとうございます!

```html
<!DOCTYPE html>
<html lang="ja">
<head>
<meta charset="utf-8">
<title>ミナテック | エアコンクリーニング・水廻りクリーニング</title>
<link href="https://fonts.googleapis.com/css2?family=M+PLUS+Rounded+1c:wght@400;700;800&family=Noto+Sans+JP:wght@400;500;700&display=swap" rel="stylesheet">
<style>
:root{
  --blue:#2d9ee3;
  --blue-dark:#1f86cc;
  --blue-light:#5ec0f0;
  --sky:#e5f3fb;
  --green:#3cb44a;
  --green-dark:#2e9a3b;
  --orange:#f07a1a;
  --red:#e8382f;
  --text:#333;
  --muted:#888;
  --white:#fff;
}
*{box-sizing:border-box;margin:0;padding:0}
html,body{width:1200px;height:2844px;overflow:hidden}
body{font-family:"Noto Sans JP",sans-serif;color:var(--text);background:var(--sky);font-size:14px;line-height:1.5}
.round{font-family:"M PLUS Rounded 1c",sans-serif}
a{color:inherit;text-decoration:none}

/* header */
.site-header{height:80px;background:var(--white);position:relative}
.tagline{position:absolute;left:24px;top:4px;font-size:10px;color:var(--muted)}
.logo{position:absolute;left:24px;top:24px;display:flex;align-items:center;gap:10px;font-family:"M PLUS Rounded 1c",sans-serif;font-weight:800;font-size:30px;color:var(--blue)}
.logo-dot{width:34px;height:34px;border-radius:50%;background:var(--blue)}
.sub-links{position:absolute;right:180px;top:8px;display:flex;gap:18px;font-size:11px;color:var(--muted)}
.cta-top{position:absolute;right:16px;top:4px;background:var(--orange);color:var(--white);font-size:11px;font-weight:700;padding:4px 12px;border-radius:3px}
.global-nav{position:absolute;right:16px;top:40px;display:flex;font-size:13px;font-weight:500}
.global-nav a{padding:8px 18px;border-left:1px solid #e3e3e3}
.global-nav a.current{background:var(--blue);color:var(--white);border-radius:3px}

/* hero */
.hero{height:560px;display:flex}
.hero-copy{width:460px;background:linear-gradient(160deg,var(--blue-light),var(--blue));color:var(--white);padding:70px 40px 0 40px}
.hero-copy .lead-pill{display:inline-block;background:var(--white);color:var(--blue);font-size:30px;font-weight:800;padding:4px 22px;border-radius:40px}
.hero-copy h1{font-size:64px;font-weight:800;line-height:1.3;margin:8px 0 22px}
.hero-copy p{font-family:"Noto Sans JP",sans-serif;font-size:13px;line-height:1.9}
.btn-outline{display:inline-block;margin-top:34px;border:2px solid var(--white);border-radius:30px;padding:8px 40px;font-size:14px;font-weight:700}
.hero-photo{flex:1;background:linear-gradient(135deg,#f3f1ec,#dfe6ea 55%,#c9d9e2)}

/* aircon */
.aircon{height:280px;position:relative}
.aircon-photo{position:absolute;left:120px;top:40px;width:480px;height:220px;background:linear-gradient(135deg,#f2f4f5,#cfdbe2)}
.aircon-text{position:absolute;left:650px;top:70px;width:380px;text-align:center}
.aircon-text small{font-size:13px;font-weight:700;color:var(--blue)}
.title-bar{display:block;margin:10px 0 14px;background:var(--white);border:3px solid var(--green);color:var(--green);font-size:30px;font-weight:800;padding:6px 0;border-radius:6px}
.btn-green{display:inline-block;background:var(--green);color:var(--white);font-weight:700;font-size:14px;padding:8px 40px;border-radius:30px}

/* campaign */
.panel{margin:0 120px;background:var(--white);border-radius:8px;overflow:hidden}
.campaign{height:372px;border:3px solid var(--green)}
.panel-head{height:50px;display:flex;align-items:center;justify-content:center;gap:12px;color:var(--white);font-size:22px;font-weight:800}
.campaign .panel-head{background:var(--green)}
.badge{background:var(--orange);color:var(--white);font-size:14px;padding:2px 10px;border-radius:4px;font-weight:800}
.price-grid{display:grid;grid-template-columns:1fr 1fr;column-gap:40px;row-gap:14px;padding:24px 50px 0}
.price-item{display:flex;align-items:center;border-bottom:1px dashed #ccc;padding-bottom:10px}
.price-item .name{flex:1;display:flex;align-items:center;gap:8px;font-size:18px;font-weight:700}
.tick{width:26px;height:26px}
.price{text-align:right}
.price s{font-size:12px;color:var(--muted)}
.price strong{display:block;font-size:36px;color:var(--red);font-weight:800;line-height:1.1}
.price strong em{font-style:normal;font-size:13px;color:var(--text);font-weight:500}
.extra{display:flex;flex-direction:column;align-items:center;margin-top:8px}
.plus{width:34px;height:34px}
.extra-row{display:flex;align-items:center;gap:16px;margin-top:4px;font-size:18px;font-weight:700}
.extra-row .tag{background:var(--blue);color:var(--white);font-size:13px;padding:3px 12px;border-radius:4px}
.extra-row strong{font-size:34px;color:var(--red);font-weight:800}

/* apply */
.apply{height:260px;margin-top:20px;border:3px solid var(--orange)}
.apply .panel-head{background:var(--orange)}
.apply-body{display:flex;height:204px}
.apply-col{flex:1;padding:26px 50px}
.apply-col + .apply-col{border-left:1px solid #eee;text-align:center}
.apply-col h3{font-size:15px;font-weight:700;margin-bottom:10px}
.tel{display:flex;align-items:center;gap:8px;font-size:34px;font-weight:800;color:var(--orange);line-height:1.3}
.tel svg{width:28px;height:28px}
.hours{font-size:12px;color:var(--muted);margin-top:4px}
.btn-orange{display:inline-block;margin-top:22px;background:var(--orange);color:var(--white);font-size:18px;font-weight:700;padding:14px 48px;border-radius:40px}

/* services */
.services{margin-top:40px;height:460px;background:var(--blue);display:flex;gap:40px;padding:40px 120px}
.service-card{flex:1;background:var(--white);border-radius:6px;overflow:hidden;text-align:center}
.service-photo{height:200px}
.service-card h3{font-size:26px;font-weight:800;color:var(--blue);line-height:1.3;margin:20px 0 18px}
.service-card .btn-green{padding:6px 34px;font-size:13px}

/* blog/news */
.posts{display:flex;gap:40px;padding:40px 120px 0;height:480px}
.post-box{flex:1;background:var(--white);border-radius:6px;overflow:hidden;text-align:center}
.post-box .panel-head{background:var(--blue);height:54px;font-size:24px}
.post-list{list-style:none;text-align:left;padding:20px 34px}
.post-list li{display:flex;gap:18px;font-size:13px;padding:16px 0;border-bottom:1px solid #eee}
.post-list time{color:var(--blue);font-weight:700;white-space:nowrap}
.btn-blue{display:inline-block;margin-top:20px;background:var(--blue);color:var(--white);font-weight:700;font-size:14px;padding:10px 60px;border-radius:30px}

/* page top */
.page-top{height:120px;display:flex;flex-direction:column;align-items:center;justify-content:center;color:var(--blue);font-size:12px;gap:4px}
.page-top svg{width:36px;height:36px}

/* footer */
.site-footer{height:164px;background:var(--blue);color:var(--white);position:relative}
.site-footer .logo{color:var(--white);top:16px;left:120px;font-size:28px}
.site-footer .logo-dot{background:var(--white)}
.address{position:absolute;left:120px;top:70px;font-size:11px;line-height:1.6}
.foot-nav{position:absolute;left:340px;top:16px;display:flex;gap:50px}
.foot-nav ul{list-style:none;font-size:11px;line-height:1.7}
.foot-nav li::before{content:"▶ ";font-size:8px}
.copy{position:absolute;bottom:6px;left:0;width:100%;text-align:center;font-size:10px;line-height:1.4}
</style>
</head>
<body>

<header class="site-header">
  <p class="tagline">大阪の清潔サービスならエアコンクリーニング専門のミナテックへ</p>
  <a class="logo" href="#"><span class="logo-dot"></span>ミナテック</a>
  <nav class="sub-links"><a href="#">お客様の声</a><a href="#">ブログ</a><a href="#">ニュース</a><a href="#">トークル</a><a href="#">フォトグラム</a></nav>
  <a class="cta-top" href="#">お申し込み・お問い合わせ</a>
  <nav class="global-nav">
    <a class="current" href="#">HOME</a><a href="#">ミナテックについて</a><a href="#">各種クリーニング</a><a href="#">料金表</a><a href="#">実績紹介</a><a href="#">よくあるご質問</a>
  </nav>
</header>

<section class="hero">
  <div class="hero-copy round">
    <span class="lead-pill">見えないところも</span>
    <h1>徹底的に!</h1>
    <p>目に見える汚れだけでなく、内部の細かな部品まで丁寧に分解・洗浄いたします。ミナテックは、暮らしの安心と快適な空気をお届けする地域密着のクリーニング専門店です。</p>
    <a class="btn-outline" href="#">ミナテックについて</a>
  </div>
  <div class="hero-photo" role="img" aria-label="明るいダイニングで家族がくつろぐ室内と、壁掛けエアコンを清掃するスタッフの写真"></div>
</section>

<section class="aircon">
  <div class="aircon-photo" role="img" aria-label="壁掛けエアコンの内部を洗浄している作業写真"></div>
  <div class="aircon-text round">
    <small>ドレンパンの分解も基本対応で安心!</small>
    <span class="title-bar">エアコンクリーニング</span>
    <a class="btn-green" href="#">詳細を見る</a>
  </div>
</section>

<section class="panel campaign">
  <div class="panel-head round"><span class="badge">お得</span>エアコンクリーニングキャンペーン</div>
  <div class="price-grid">
    <div class="price-item"><span class="name"><svg class="tick" viewBox="0 0 26 26"><circle cx="13" cy="13" r="13" fill="#3cb44a"/><path d="M7 13l4 4 8-8" stroke="#fff" stroke-width="3" fill="none"/></svg>通常エアコン室内機</span><span class="price"><s>通常価格¥11,664</s><strong>¥10,000<em>(税込)</em></strong></span></div>
    <div class="price-item"><span class="name"><svg class="tick" viewBox="0 0 26 26"><circle cx="13" cy="13" r="13" fill="#3cb44a"/><path d="M7 13l4 4 8-8" stroke="#fff" stroke-width="3" fill="none"/></svg>エアコン室外機</span><span class="price"><s>通常価格¥7,344</s><strong>¥3,000<em>(税込)</em></strong></span></div>
    <div class="price-item"><span class="name"><svg class="tick" viewBox="0 0 26 26"><circle cx="13" cy="13" r="13" fill="#3cb44a"/><path d="M7 13l4 4 8-8" stroke="#fff" stroke-width="3" fill="none"/></svg>お掃除機能付室内機</span><span class="price"><s>通常価格¥28,520</s><strong>¥18,000<em>(税込)</em></strong></span></div>
    <div class="price-item"><span class="name"><svg class="tick" viewBox="0 0 26 26"><circle cx="13" cy="13" r="13" fill="#3cb44a"/><path d="M7 13l4 4 8-8" stroke="#fff" stroke-width="3" fill="none"/></svg>防カビコーティング</span><span class="price"><s>通常価格¥7,344</s><strong>¥3,000<em>(税込)</em></strong></span></div>
  </div>
  <div class="extra">
    <svg class="plus" viewBox="0 0 34 34"><circle cx="17" cy="17" r="17" fill="#2d9ee3"/><path d="M17 8v18M8 17h18" stroke="#fff" stroke-width="4"/></svg>
    <div class="extra-row"><span class="tag">さらに今なら</span>2台目以降は<strong>¥500OFF</strong></div>
  </div>
</section>

<section class="panel apply">
  <div class="panel-head round">いますぐクリーニングを申し込む</div>
  <div class="apply-body">
    <div class="apply-col">
      <h3>お電話での申し込みはこちら</h3>
      <p class="tel"><svg viewBox="0 0 24 24"><path fill="#f07a1a" d="M6.6 10.8a15 15 0 006.6 6.6l2.2-2.2a1 1 0 011-.25 11.4 11.4 0 003.6.57 1 1 0 011 1V20a1 1 0 01-1 1A17 17 0 013 4a1 1 0 011-1h3.5a1 1 0 011 1c0 1.25.2 2.45.57 3.6a1 1 0 01-.25 1z"/></svg>050-4812-7736</p>
      <p class="tel"><svg viewBox="0 0 24 24"><path fill="#f07a1a" d="M6.6 10.8a15 15 0 006.6 6.6l2.2-2.2a1 1 0 011-.25 11.4 11.4 0 003.6.57 1 1 0 011 1V20a1 1 0 01-1 1A17 17 0 013 4a1 1 0 011-1h3.5a1 1 0 011 1c0 1.25.2 2.45.57 3.6a1 1 0 01-.25 1z"/></svg>080-2957-3418</p>
      <p class="hours">受付時間 9:00〜19:00(年中無休)</p>
    </div>
    <div class="apply-col">
      <h3>フォームからのお問い合わせはこちら</h3>
      <a class="btn-orange" href="#">✉ お問い合わせフォーム</a>
    </div>
  </div>
</section>

<section class="services">
  <article class="service-card"><div class="service-photo" role="img" aria-label="清潔に磨かれた洗面台の写真" style="background:linear-gradient(135deg,#eef2f3,#c5d2d8)"></div><h3 class="round">水廻り<br>クリーニング</h3><a class="btn-green" href="#">詳細を見る</a></article>
  <article class="service-card"><div class="service-photo" role="img" aria-label="窓や室内をスプレーで掃除する手元の写真" style="background:linear-gradient(135deg,#dde7ec,#9fb4c0)"></div><h3 class="round">その他<br>クリーニング</h3><a class="btn-green" href="#">詳細を見る</a></article>
  <article class="service-card"><div class="service-photo" role="img" aria-label="コーティング仕上げのキッチンシンクの写真" style="background:linear-gradient(135deg,#f4f4f2,#cfd4d6)"></div><h3 class="round">水廻り<br>コーティング</h3><a class="btn-green" href="#">詳細を見る</a></article>
  <article class="service-card"><div class="service-photo" role="img" aria-label="艶のある木目フローリングの写真" style="background:linear-gradient(135deg,#e9d6b8,#c49a66)"></div><h3 class="round">フロア<br>コーティング</h3><a class="btn-green" href="#">詳細を見る</a></article>
</section>

<section class="posts">
  <div class="post-box">
    <div class="panel-head round">ブログ</div>
    <ul class="post-list">
      <li><time>2017年9月25日</time>エアコン内部の分解洗浄を行いました</li>
      <li><time>2017年5月12日</time>メーカー製エアコン室外機掃除</li>
      <li><time>2017年5月9日</time>完全分解洗浄の作業事例</li>
    </ul>
    <a class="btn-blue" href="#">もっと見る</a>
  </div>
  <div class="post-box">
    <div class="panel-head round">お知らせ</div>
    <ul class="post-list">
      <li><time>2018年4月2日</time>エアコンクリーニングキャンペーン開始!</li>
      <li><time>2017年4月26日</time>エアコンクリーニングキャンペーン終了</li>
      <li><time>2017年3月9日</time>エアコンクリーニングキャンペーン開始!</li>
    </ul>
    <a class="btn-blue" href="#">もっと見る</a>
  </div>
</section>

<a class="page-top" href="#"><svg viewBox="0 0 36 36"><circle cx="18" cy="18" r="17" fill="none" stroke="#2d9ee3" stroke-width="2"/><path d="M11 21l7-7 7 7" stroke="#2d9ee3" stroke-width="3" fill="none"/></svg>ページトップへ</a>

<footer class="site-footer">
  <a class="logo" href="#"><span class="logo-dot"></span>ミナテック</a>
  <p class="address">〒540-0000<br>大阪府大阪市中央区港町1-2-3<br>TEL 050-4812-7736<br>携帯 080-2957-3418</p>
  <nav class="foot-nav">
    <ul><li>HOME</li><li>ミナテックについて</li></ul>
    <ul><li>サービス</li><li>エアコンクリーニング</li><li>水廻りクリーニング</li><li>その他クリーニング</li><li>水廻りコーティング</li><li>フロアコーティング</li></ul>
    <ul><li>料金表</li><li>実績紹介</li><li>お申し込みの流れ</li><li>よくあるご質問</li><li>お申し込み・お問い合わせ</li></ul>
    <ul><li>ニュース</li><li>ブログ</li><li>お客様の声</li><li>トークル</li><li>フォトグラム</li></ul>
  </nav>
  <p class="copy">© Minatec. All Rights Reserved.</p>
</footer>

</body>
</html>
```